Proposal Microsoft Word Template

We are looking for a professional, 5 page document to import our proposals onto. We are looking for a cover page with plenty of color and design built around and utilizing our logo. The remaining four pages should utilize our logo and have some design elements to make it stand apart from other formal proposals. We aren't sure what this looks like yet, so we are open to plenty of ideas. I will upload our logo for your use. We are a fire protection company that sells primarily to other commercial clientele.

First page will be the cover page. This should have our logo prominently placed. A place for the clients name and info.
Second page will be the Executive Summary. Smaller logo, possibly a border on this page, and a clean colorful ribbon on the footer with our information on the bottom. I do like red, blue and black for colors.

Third page will be material lists and pricing information

4th page will consist of detailed scope of work, and exclusions
Fifth page will consist of terms and conditions

Target Market(s)

Commercial Industrial Government Sectors

Requirements
Must have
• Color, clean lines and formatting.

```html
<!DOCTYPE html>
<html lang="en">
<head>
<meta charset="utf-8">
<title>Bastion Fire &amp; Safety — Proposal Template</title>
<link rel="stylesheet" href="https://fonts.googleapis.com/css2?family=Saira:wght@300;400;500;700;800&display=swap">
<style>
:root{
  --red:#e31b23;
  --ink:#111111;
  --text:#3a3a3a;
  --paper:#ffffff;
  --stage-top:#666666;
  --stage-bottom:#444444;
  --night:#1d0c10;
  --bar-dark:#555555;
  --bar-light:#8a8a8a;
}
*{margin:0;padding:0;box-sizing:border-box}
html,body{width:1200px;height:960px;overflow:hidden}
body{
  background:radial-gradient(ellipse at 50% 0%,var(--stage-top),var(--stage-bottom) 75%);
  font-family:"Saira",Arial,sans-serif;
  position:relative;
}
.page{
  position:absolute;top:113px;width:525px;height:743px;
  background:var(--paper);
  box-shadow:0 2px 10px rgba(0,0,0,.35);
  overflow:hidden;
}
.cover{left:57px}
.summary{left:605px}

/* brand name */
.brand{
  position:absolute;color:var(--red);font-weight:800;
  letter-spacing:.02em;white-space:nowrap;text-transform:uppercase;line-height:1;
}
.cover .brand{left:0;right:0;top:152px;text-align:center;font-size:27px}
.cover .brand-rule{position:absolute;left:114px;right:115px;top:199px;height:2px;background:var(--ink)}

/* hero */
.hero-photo{
  position:absolute;left:0;top:346px;width:525px;height:354px;
  background:
    radial-gradient(ellipse at 55% 75%,rgba(230,40,50,.55),transparent 45%),
    radial-gradient(ellipse at 20% 40%,rgba(200,40,50,.45),transparent 40%),
    radial-gradient(ellipse at 85% 35%,rgba(200,40,50,.4),transparent 40%),
    linear-gradient(180deg,#2a0f14,var(--night) 60%,#140709);
}
.services{position:absolute;left:0;top:317px;width:525px}
.service{position:absolute;width:120px;text-align:center;transform:translateX(-50%)}
.service .badge{width:63px;height:63px;border-radius:50%;background:var(--red);margin:0 auto;display:flex;align-items:center;justify-content:center}
.service .label{margin-top:10px;color:#fff;font-weight:700;font-size:14px;line-height:16px;text-transform:uppercase}
.client-name{position:absolute;left:0;right:0;top:627px;text-align:center;color:#fff;font-size:22px;font-weight:400;letter-spacing:.02em}
.contact-row{position:absolute;display:flex;justify-content:space-between;align-items:center;color:#fff;font-size:12.5px;font-weight:400;white-space:nowrap}
.cover .contact-row{left:24px;right:23px;top:665px}
.contact-row span{display:flex;align-items:center;gap:5px}
.contact-row svg{width:9px;height:9px;fill:currentColor;flex:none}
.follow{position:absolute;right:25px;top:714px;display:flex;align-items:center;gap:5px;font-size:9.5px;color:var(--ink);text-transform:uppercase}
.follow i{display:block;width:17px;height:17px;border-radius:50%;background:var(--red)}
.follow i:first-of-type{margin-left:3px}

/* summary page */
.summary .brand{right:19px;top:30px;font-size:12px}
.summary .brand-rule{position:absolute;right:19px;top:47px;width:146px;height:1.5px;background:var(--ink)}
.frame{position:absolute;left:10px;top:79px;width:506px;height:654px;border:1px solid var(--red);border-radius:14px;overflow:hidden}
.section-title{position:absolute;left:37px;top:132px;color:var(--red);font-weight:800;font-size:23px;line-height:23px;text-transform:uppercase}
.body-copy{position:absolute;left:208px;top:30px;width:282px;color:var(--text);font-size:11px;line-height:13px;text-align:justify}
.body-copy p+p{margin-top:13px}
.info-ribbon{position:absolute;left:0;right:0;top:601px;height:40px;background:linear-gradient(90deg,var(--bar-dark),var(--bar-light) 35%,var(--bar-dark) 60%,var(--bar-light));}
.info-ribbon .contact-row{left:14px;right:14px;top:11px;font-size:12px}
</style>
</head>
<body>

<section class="page cover">
  <div class="brand">Bastion Fire &amp; Safety</div>
  <div class="brand-rule"></div>

  <div class="hero-photo" role="img" aria-label="Night city street with blurred red traffic lights"></div>

  <div class="services">
    <div class="service" style="left:82px">
      <div class="badge"><svg width="30" height="36" viewBox="0 0 30 36" fill="#fff"><rect x="9" y="8" width="12" height="26" rx="4"/><rect x="12" y="3" width="6" height="5"/><path d="M18 4h8v3h-6z"/><path d="M9 12 4 24h3l3-8z"/></svg></div>
      <div class="label">Fire<br>Protection</div>
    </div>
    <div class="service" style="left:210px">
      <div class="badge"><svg width="26" height="32" viewBox="0 0 26 32"><path d="M7 14V9a6 6 0 0 1 12 0v5" fill="none" stroke="#fff" stroke-width="3"/><rect x="3" y="14" width="20" height="16" rx="2" fill="#fff"/><circle cx="13" cy="21" r="2.5" fill="#e31b23"/><rect x="12" y="22" width="2" height="4" fill="#e31b23"/></svg></div>
      <div class="label">Security</div>
    </div>
    <div class="service" style="left:326px">
      <div class="badge"><svg width="38" height="36" viewBox="0 0 38 36"><path d="M6 20a13 13 0 0 1 26 0" fill="none" stroke="#fff" stroke-width="3"/><rect x="3" y="18" width="7" height="11" rx="2" fill="#fff"/><rect x="28" y="18" width="7" height="11" rx="2" fill="#fff"/><path d="M31 29q0 5-9 5" fill="none" stroke="#fff" stroke-width="2"/><circle cx="19" cy="20" r="8" fill="#fff"/><text x="19" y="23" font-size="7.5" font-weight="700" text-anchor="middle" fill="#e31b23" font-family="Saira,Arial,sans-serif">24h</text></svg></div>
      <div class="label">24/7<br>Support</div>
    </div>
    <div class="service" style="left:446px">
      <div class="badge"><svg width="24" height="32" viewBox="0 0 24 32"><path d="M12 1a11 11 0 0 0-11 11c0 8 11 19 11 19s11-11 11-19A11 11 0 0 0 12 1z" fill="#fff"/><circle cx="12" cy="12" r="4.5" fill="#e31b23"/></svg></div>
      <div class="label">Unlimited<br>Access</div>
    </div>
  </div>

  <div class="client-name">DANA WHITCOMBE</div>
  <div class="contact-row">
    <span><svg viewBox="0 0 10 10"><path d="M0 2h10v6H0z"/></svg>dwhitcombe@bastionsafety.com</span>
    <span><svg viewBox="0 0 10 10"><path d="M1 5q0-3 4-3t4 3H7V4H3v1zM2 6h6l1 3H1z"/></svg>1-800-555-0147</span>
    <span><svg viewBox="0 0 10 10"><circle cx="5" cy="5" r="4.5"/></svg>www.bastionsafety.com</span>
  </div>
  <div class="follow">Follow us on <i></i><i></i></div>
</section>

<section class="page summary">
  <div class="brand">Bastion Fire &amp; Safety</div>
  <div class="brand-rule"></div>
  <div class="frame">
    <h2 class="section-title">Executive<br>Summary</h2>
    <div class="body-copy">
      <p>Lorem ipsum dolor sit amet, consectetur adipiscing elit, sed do eiusmod tempor incididunt ut labore et dolore magna aliqua. Ut enim ad minim veniam, quis nostrud exercitation ullamco laboris nisi ut aliquip ex ea commodo consequat. Duis aute irure dolor in reprehenderit in voluptate velit esse cillum dolore eu fugiat nulla pariatur. Excepteur sint occaecat cupidatat non proident, sunt in culpa qui officia deserunt mollit anim id est laborum.</p>
      <p>Lorem ipsum dolor sit amet, consectetur adipiscing elit, sed do eiusmod tempor incididunt ut labore et dolore magna aliqua. Ut enim ad minim veniam, quis nostrud exercitation ullamco laboris nisi ut aliquip ex ea commodo consequat. Duis aute irure dolor in reprehenderit in voluptate velit esse cillum dolore eu fugiat nulla pariatur. Excepteur sint occaecat cupidatat non proident, sunt in culpa qui officia deserunt mollit anim id est laborum.</p>
    </div>
    <div class="info-ribbon">
      <div class="contact-row">
        <span><svg viewBox="0 0 10 10"><path d="M0 2h10v6H0z"/></svg>dwhitcombe@bastionsafety.com</span>
        <span><svg viewBox="0 0 10 10"><path d="M1 5q0-3 4-3t4 3H7V4H3v1zM2 6h6l1 3H1z"/></svg>1-800-555-0147</span>
        <span><svg viewBox="0 0 10 10"><circle cx="5" cy="5" r="4.5"/></svg>www.bastionsafety.com</span>
      </div>
    </div>
  </div>
</section>

</body>
</html>
```